Redesign website for small print company

Vindaborgprent is a small printing company in Iceland mainly servicing Students, schools, etc. We are also doing all kind of other jobs, like business cards, book printing, brochure printing etc. We are also selling books online.
Our website is: www.vindaborgprent.is
What we are looking for is:
- Web Design (Uncoded - PSD layout only)
- Mobile friendly design, using our current color scheme: Red, green, yellow and light gray.
- Clean simple design
- Simple, light and easy to use.
- More menu Items/drop down
Industry/Entity Type
Digital Printing
Number of Pages Required
5+ page
Requirements
Must have
- Easy navigation
- Designed for mobile
- Current color scheme (see logo)
Nice to have
- Icon based products

```html
<!DOCTYPE html>
<html lang="en">
<head>
<meta charset="utf-8">
<title>Vindaborgprent</title>
<link rel="stylesheet" href="https://fonts.googleapis.com/css2?family=Lato:wght@300;400;700;900&display=swap">
<style>
:root{
  --yellow:#f5c800;
  --green:#1f7a3c;
  --red:#e8453c;
  --ink:#2b2d42;
  --navy:#34324f;
  --navy-dark:#2c2a45;
  --light-gray:#ebebeb;
  --mid-gray:#8a8a8a;
  --white:#ffffff;
}
*{box-sizing:border-box;margin:0;padding:0}
html,body{width:1200px;height:3030px;overflow:hidden}
body{position:relative;font-family:"Lato",sans-serif;color:var(--ink);background:var(--white)}

/* Header */
.site-header{position:absolute;left:0;top:0;width:1200px;height:127px;background:var(--white)}
.brand{position:absolute;left:52px;top:44px;display:flex;align-items:center;gap:12px}
.brand-mark{width:34px;height:34px;background:var(--red)}
.brand-name{font-weight:900;font-size:26px;color:var(--ink);letter-spacing:.5px}
.main-nav{position:absolute;left:378px;top:54px;display:flex;gap:36px;font-size:16px;font-weight:400;text-transform:uppercase;color:var(--ink)}
.main-nav .active{color:var(--yellow)}
.header-contact{position:absolute;left:812px;top:0;width:388px;height:127px;border-left:1px solid #dcdcdc}
.lang{position:absolute;top:66px;width:38px;height:26px}
.lang-is{left:40px;background:#0b4ea2}
.lang-en{left:92px;background:#1c3f94}
.lang-is::before,.lang-en::before{content:"";position:absolute;left:0;right:0;top:10px;height:6px;background:var(--white)}
.lang-is::after,.lang-en::after{content:"";position:absolute;top:0;bottom:0;left:12px;width:6px;background:var(--white)}
.lang-en::after{left:16px}
.contact-line{position:absolute;left:160px;font-size:16px;color:var(--ink);display:flex;align-items:center;gap:10px}
.contact-line svg{width:16px;height:16px}
.contact-email{top:50px}
.contact-phone{top:78px}

/* Hero */
.hero{position:absolute;left:0;top:127px;width:1200px;height:668px;overflow:hidden}
.hero-photo{position:absolute;inset:0;background:linear-gradient(120deg,#6a6a72 0%,#9a9aa2 30%,#c9c9cc 55%,#8d8d95 80%,#5a5a62 100%)}
.hero-photo::after{content:"";position:absolute;inset:0;background:linear-gradient(180deg,rgba(0,0,0,.25),rgba(0,0,0,.05) 60%,rgba(255,255,255,.15))}
.hero-kicker{position:absolute;left:0;width:1200px;top:150px;text-align:center;color:var(--white);font-weight:300;font-size:34px;letter-spacing:1px}
.hero-title{position:absolute;left:0;width:1200px;top:188px;text-align:center;color:var(--white);font-weight:900;font-size:52px;letter-spacing:.5px}
.action{position:absolute;top:284px;width:190px;text-align:center}
.action-icon{width:190px;height:190px;border-radius:50%;display:flex;align-items:center;justify-content:center}
.action-icon svg{width:96px;height:96px}
.action-label{margin-top:18px;color:var(--white);font-size:22px;font-weight:400;text-transform:uppercase}
.action-send{left:253px}.action-send .action-icon{background:var(--yellow)}
.action-design{left:480px}.action-design .action-icon{background:var(--green)}
.action-offers{left:708px}.action-offers .action-icon{background:var(--red)}

/* Products */
.products-title{position:absolute;left:0;width:1200px;top:852px;text-align:center;font-weight:700;font-size:40px;color:var(--ink)}
.product{position:absolute;width:346px;height:346px;border-radius:50%;overflow:hidden}
.product-photo{position:absolute;inset:0;background:radial-gradient(circle at 40% 35%,#f2f2f2,#c9c9c9 70%,#a8a8a8)}
.product-band{position:absolute;left:0;right:0;top:235px;height:70px;background:var(--yellow);display:flex;align-items:center;justify-content:center;color:var(--white);font-weight:900;font-size:34px;text-transform:uppercase}
.p1{left:54px;top:963px}.p2{left:427px;top:963px}.p3{left:800px;top:963px}
.p4{left:54px;top:1342px}.p5{left:427px;top:1342px}.p6{left:800px;top:1342px}
.p3 .product-photo{background:radial-gradient(circle at 40% 35%,#e9e2dc,#b59a8a 70%,#8d7566)}
.p4 .product-photo{background:radial-gradient(circle at 40% 35%,#bfc5b8,#7c8677 70%,#5c6358)}
.p5 .product-photo{background:radial-gradient(circle at 40% 35%,#f0e4e4,#d8a9a9 70%,#b88b8b)}
.p2 .product-photo{background:radial-gradient(circle at 40% 35%,#e8eef2,#b8c8d2 70%,#8fa4b0)}

/* About */
.about{position:absolute;left:0;top:1810px;width:1200px;height:645px;background:var(--light-gray)}
.about-title{position:absolute;left:50px;top:72px;font-weight:700;font-size:40px;color:var(--ink)}
.about-text{position:absolute;left:55px;top:190px;width:540px;font-size:14.5px;line-height:1.55;color:var(--ink)}
.about-text p{margin-bottom:20px}
.about-brand{position:absolute;left:790px;top:120px;width:320px;display:flex;flex-direction:column;align-items:center;gap:30px}
.about-brand-mark{width:230px;height:230px;background:var(--red)}
.about-brand-name{font-weight:900;font-size:40px;color:var(--ink)}

/* Footer */
.site-footer{position:absolute;left:0;top:2455px;width:1200px;height:575px;background:var(--navy)}
.footer-map{position:absolute;left:60px;top:60px;width:850px;height:400px;background:radial-gradient(ellipse at 45% 50%,#44426a,var(--navy) 75%);opacity:.9}
.footer-address{position:absolute;left:372px;top:118px;display:flex;gap:12px;color:var(--white);font-weight:700;font-size:16px;line-height:1.4}
.footer-address svg{width:30px;height:40px;flex:none}
.footer-nav{position:absolute;right:95px;top:118px;text-align:right;color:var(--white)}
.footer-nav h3{font-size:18px;font-weight:400;margin-bottom:26px}
.footer-nav li{list-style:none;font-size:14px;line-height:30px}
.social{position:absolute;right:100px;top:340px;display:flex;gap:18px}
.social span{width:14px;height:14px;border-radius:50%;background:var(--yellow)}
.back-top{position:absolute;right:100px;top:410px;font-size:12px;color:var(--white);opacity:.8}
.footer-mark{position:absolute;left:585px;top:453px;width:30px;height:34px;background:var(--white)}
.copyright{position:absolute;left:0;width:1200px;top:503px;text-align:center;font-size:13px;color:var(--white)}
</style>
</head>
<body>

<header class="site-header">
  <div class="brand"><span class="brand-mark"></span><span class="brand-name">VINDABORGPRENT</span></div>
  <nav class="main-nav"><span class="active">Home</span><span>Service</span><span>Job Submit</span><span>About Us</span></nav>
  <div class="header-contact">
    <span class="lang lang-is" role="img" aria-label="Icelandic language"></span>
    <span class="lang lang-en" role="img" aria-label="English language"></span>
    <div class="contact-line contact-email">
      <svg viewBox="0 0 16 16"><rect x="1" y="3" width="14" height="10" fill="#2b2d42"/><path d="M1 3l7 6 7-6" stroke="#fff" stroke-width="1.5" fill="none"/></svg>
      verk@vindaborgprent.is
    </div>
    <div class="contact-line contact-phone">
      <svg viewBox="0 0 16 16"><path d="M3 1l3 0 1 4-2 1c1 2 3 4 5 5l1-2 4 1v3c0 1-1 2-2 2C7 15 1 9 1 3c0-1 1-2 2-2z" fill="#2b2d42"/></svg>
      555-0142
    </div>
  </div>
</header>

<section class="hero">
  <div class="hero-photo" role="img" aria-label="Fanned colour swatch guide on a desk"></div>
  <p class="hero-kicker">BEST IN QUALITY</p>
  <h1 class="hero-title">BEST IN BUSINESS</h1>
  <div class="action action-send">
    <div class="action-icon"><svg viewBox="0 0 100 100"><path d="M90 12L8 48l28 10 6 30 14-20 20 14z" fill="#fff"/><path d="M36 58L90 12 44 64" fill="none" stroke="#f5c800" stroke-width="4"/></svg></div>
    <p class="action-label">Send Work</p>
  </div>
  <div class="action action-design">
    <div class="action-icon"><svg viewBox="0 0 100 100"><path d="M50 10C26 10 10 28 10 48c0 20 16 34 32 34 8 0 8-8 4-12-4-4 0-10 6-10h12c14 0 26-8 26-22C90 22 72 10 50 10z" fill="#fff"/><circle cx="30" cy="44" r="6" fill="#1f7a3c"/><circle cx="44" cy="28" r="6" fill="#1f7a3c"/><circle cx="64" cy="28" r="6" fill="#1f7a3c"/><circle cx="76" cy="44" r="6" fill="#1f7a3c"/></svg></div>
    <p class="action-label">Design Work</p>
  </div>
  <div class="action action-offers">
    <div class="action-icon"><svg viewBox="0 0 100 100"><path d="M14 14h36l40 40-36 36-40-40z" fill="#fff"/><circle cx="32" cy="32" r="7" fill="#e8453c"/></svg></div>
    <p class="action-label">Get Offers</p>
  </div>
</section>

<h2 class="products-title">Products</h2>
<div class="product p1"><div class="product-photo" role="img" aria-label="Essay pages with yellow document icon"></div><div class="product-band">Essays</div></div>
<div class="product p2"><div class="product-photo" role="img" aria-label="Business cards with yellow card icon"></div><div class="product-band">Business Cards</div></div>
<div class="product p3"><div class="product-photo" role="img" aria-label="Folded leaflets with yellow leaflet icon"></div><div class="product-band">Leaflets</div></div>
<div class="product p4"><div class="product-photo" role="img" aria-label="Printing press with yellow printer icon"></div><div class="product-band">Book Printing</div></div>
<div class="product p5"><div class="product-photo" role="img" aria-label="Printed posters with yellow poster icon"></div><div class="product-band">Posters</div></div>
<div class="product p6"><div class="product-photo" role="img" aria-label="Stack of textbooks with yellow open book icon"></div><div class="product-band">Textbooks</div></div>

<section class="about">
  <h2 class="about-title">About Us</h2>
  <div class="about-text">
    <p>Vindaborgprent is a print shop based on the university campus that focuses on serving students and staff, while also offering general printing to the public.</p>
    <p>We print reports, theses and course material for schools and students, together with business cards, posters, leaflets, booklets and bound books. We also handle scanning, binding, laminating and large format jobs for teachers, companies and institutions.</p>
    <p>Vindaborgprent is a certified green print shop. The certification is a respected Nordic environmental label that has set down roots here and is well known.</p>
    <p>Vindaborgprent is located on the corner of Hlíðarvegur and Sólgata (entrance from Sólgata).</p>
  </div>
  <div class="about-brand"><span class="about-brand-mark"></span><span class="about-brand-name">VINDABORGPRENT</span></div>
</section>

<footer class="site-footer">
  <div class="footer-map" role="img" aria-label="Dotted world map"></div>
  <div class="footer-address">
    <svg viewBox="0 0 30 40"><path d="M15 1C7 1 1 7 1 15c0 10 14 24 14 24s14-14 14-24C29 7 23 1 15 1z" fill="#f5c800"/><circle cx="15" cy="15" r="5" fill="#34324f"/></svg>
    <div>Hlíðarvegur 7, Reykjavik<br>Iceland</div>
  </div>
  <nav class="footer-nav">
    <h3>Navigation</h3>
    <ul><li>Home</li><li>Service</li><li>Job Submit</li><li>Contact</li></ul>
  </nav>
  <div class="social"><span></span><span></span><span></span></div>
  <p class="back-top">Back to Top</p>
  <span class="footer-mark"></span>
  <p class="copyright">Copyright 2018 Vindaborgprent</p>
</footer>

</body>
</html>
```